Tova Brisk Fitness Coaching Project

I am a personal trainer based in London. My services include one-on-one PT sessions, bootcamps.
I would like the design to be minimalistic. With light colours: white, pink, purple.
I specialise in weight loss, flexibility, mobility.

Tova Penrick
Personal Trainer
Email: tova.penrick@mailgrove.net
tel: 07500 918 243
Instagram: Tova Brisk

Target Market(s)

adults, mostly females (age 18-50).

Industry/Entity Type

Fitness

Contact Information for Business Card

Tova Penrick
Personal Trainer
tel: 07500 918 243
Instagram: Tova Brisk

Font styles to use
Serif

Colors
eea4c8
fbd4d5
fdf9cf
cfeae6
cee9f5

Requirements
Nice to have
• minimalistic style
• easy to read and remember

```html
<!DOCTYPE html>
<html lang="en">
<head>
<meta charset="utf-8">
<title>Tova Penrick – Business Card</title>
<link href="https://fonts.googleapis.com/css2?family=Jost:wght@300;400&display=swap" rel="stylesheet">
<style>
  :root {
    --backdrop: #ecebe8;
    --card-white: #ffffff;
    --pink: #eea4c8;
    --mint: #cfeae6;
    --photo-top: #5b302c;
    --photo-mid: #3e2a28;
    --photo-bottom: #2b2828;
    --light-text: #ffffff;
  }
  * { margin: 0; padding: 0; box-sizing: border-box; }
  html, body {
    width: 1200px;
    height: 900px;
    overflow: hidden;
    background: var(--backdrop);
  }
  .stage {
    position: relative;
    width: 1200px;
    height: 900px;
    display: flex;
    justify-content: center;
    align-items: center;
    gap: 80px;
  }
  .card {
    width: 330px;
    height: 578px;
    position: relative;
    box-shadow: 0 6px 18px rgba(0,0,0,0.12);
  }
  .card-front {
    background: var(--card-white);
    color: var(--pink);
    font-family: "Jost", sans-serif;
    font-weight: 400;
    text-align: center;
  }
  .front-name {
    position: absolute;
    top: 210px;
    left: 0;
    right: 0;
    font-size: 29px;
    letter-spacing: 0.2em;
    text-transform: uppercase;
  }
  .contact-block {
    position: absolute;
    top: 300px;
    left: 0;
    right: 0;
    display: flex;
    flex-direction: column;
    align-items: center;
  }
  .contact-name {
    font-size: 19px;
    letter-spacing: 0.14em;
  }
  .contact-role {
    font-size: 11px;
    letter-spacing: 0.22em;
    margin-top: 1px;
  }
  .contact-icons {
    display: flex;
    gap: 7px;
    margin: 12px 0 10px;
  }
  .contact-icons svg { width: 11px; height: 11px; }
  .contact-line {
    font-size: 12.5px;
    letter-spacing: 0.16em;
    line-height: 1.55;
  }
  .card-back {
    border: 7px solid var(--mint);
    background: var(--mint);
  }
  .back-photo {
    position: absolute;
    inset: 0;
    background: linear-gradient(180deg, var(--photo-top) 0%, var(--photo-mid) 55%, var(--photo-bottom) 100%);
  }
  .back-name {
    position: absolute;
    top: 262px;
    left: 0;
    right: 0;
    text-align: center;
    font-family: "Jost", sans-serif;
    font-weight: 300;
    font-size: 28px;
    letter-spacing: 0.2em;
    color: var(--light-text);
  }
</style>
</head>
<body>
  <main class="stage">
    <section class="card card-front">
      <h1 class="front-name">Tova Penrick</h1>
      <div class="contact-block">
        <p class="contact-name">Tova Penrick</p>
        <p class="contact-role">Personal Trainer</p>
        <div class="contact-icons">
          <svg viewBox="0 0 12 12" aria-label="phone">
            <path d="M3 1 L4.6 3.4 L3.6 4.6 Q4.6 6.8 7.2 8.2 L8.4 7.2 L11 8.8 L10 11 Q4.5 10.5 1 3 Z" fill="var(--pink)"/>
          </svg>
          <svg viewBox="0 0 12 12" aria-label="email">
            <rect x="1" y="2.5" width="10" height="7" fill="none" stroke="var(--pink)" stroke-width="1.2"/>
            <path d="M1 2.5 L6 7 L11 2.5" fill="none" stroke="var(--pink)" stroke-width="1.2"/>
          </svg>
          <svg viewBox="0 0 12 12" aria-label="social profile">
            <rect x="1.5" y="1.5" width="9" height="9" fill="none" stroke="var(--pink)" stroke-width="1.3"/>
          </svg>
        </div>
        <p class="contact-line">07500 918 243</p>
        <p class="contact-line">tova.penrick@mailgrove.net</p>
        <p class="contact-line">Tova Brisk</p>
      </div>
    </section>

    <section class="card card-back">
      <div class="back-photo" role="img" aria-label="Photo of the trainer doing a handstand split in front of a dark wooden door on a red wall"></div>
      <h2 class="back-name">TOVA PENRICK</h2>
    </section>
  </main>
</body>
</html>
```